Lotvantage.com Webpage Design

Design Brief for lotvantage.com (Copy of Brief also in attached Word file)

Name of Website- lotvantage.com (existing logo and look & feel of website to be changed)

Logo - Finalised. The logo files are attached with the brief as “logo.jpeg”. The “Blue- Grey” version of the logo is for use on lighter backgrounds and the “Orange-White” version of the logo is for use on darker backgrounds. (A full Black version of the logo is also attached). Both versions may be used in different parts of the website. All attached files are in .png format.
Status - The website in functional and is undergoing user trials. However, we want to improve the look & feel of the website so at it seems
a. cotemporary,
b. Easy to Navigate
c. professional and
d. Vibrant.

Please visit ‘lotvantage.com’ to check out the website and its functionalities – please use it only as a reference for the features & functions to be provided, however the designer should use a ‘Free Hand’ in designing the composition of various parts of the webpage without getting too influenced by the existing design

Objective of the Website ‘lotvantage.com –
a. It is a portal focussed on listing of ‘Retail’ specific real-estate properties by developers, owners and realty brokers. The properties shall listed under the following four categories-
i. Retail Malls
ii. Shopping Complexes
iii. High-street shops
iv. Retail Warehouses
*refer lotvantage.com for better clarity

b. The abovementioned properties shall be listed either for ‘Sale’ or ‘rent\lease’ or both

c. Users shall visit the site in case they wish to acquire a retail \ shop space either on ‘sale’ or ‘rent’. These Users would be able to specify the ‘Search Criteria’ through the tool-bars provided on the website – the ‘Search Criteria’ shall comprise of ‘Type of space category’, ‘City’, ‘Locality’, transaction type ie ‘Rent \ Sale’ and ‘Area Range’

d. The main revenue model for the website shall be listing fee ( or advertising charges ) payable by those listing their properties on the website.

Three Main Pages of Website (lotvantage.com) that need to be designed -
a. Main Home Page (visit the web link - http://lotvantage.com/ ) - The main home page has the “Search Toolbar” for specifying of Search Criteria by the User. It shall also have the following features & functions-
i. Main Advertising Banner
ii. Featured Projects
iii. New Launches
iv. Toolbar with buttons – ‘Advertise with Us’, ‘Listings Alert’, ‘Lot Mavens’, ‘Advertiser Login’

b. Property Listings Page (visit the web link - http://lotvantage.com/gurgaon-in-india ) - The List of property options that match the Criteria specified by the ‘User’ get displayed on this page.

c. Property Detail Page - When the ‘User’ clicks on the “More….” Button on the ‘Property Listings Page’ (given in point b. above) the web page with the details of the property opens. (For Example – visit the web link - http://lotvantage.com/brevo-Shopping-Complex-brevo-quadrel-gurgaon-636 )

Note:- Please refer to attached ‘Shopping’ related images the designer may use them on the website to provide a look & feel of retail if required – either separately or rotate in a single window

Target Market(s)

Retailers & Investors looking for retail space, Real Estate Brokers, Developers

Industry/Entity Type

Advertising

Number of Pages Required

3 page

Requirements
Must have
• Refer to existing site lotvantage.com -- all the existing functionalities are a must have.
Nice to have
• The Designer may use the retail related images on the website if required for making it more vibrant. Refer attached images Shopping(1-6).jpg

```html
<!DOCTYPE html>
<html lang="en">
<head>
<meta charset="utf-8">
<title>Lotvantage.com – Retail Space Portal</title>
<link href="https://fonts.googleapis.com/css2?family=Open+Sans:wght@400;600;700&display=swap" rel="stylesheet">
<style>
:root{
  --blue:#1a8ee0;
  --blue-dark:#0f63a8;
  --navy:#123f6e;
  --ink:#2b2b2b;
  --grey-text:#6b6b6b;
  --line:#dcdcdc;
  --panel:#5b5b5b;
  --panel-dark:#3e3e3e;
  --footer:#4a4a4a;
  --white:#ffffff;
  --accent:#e07b1a;
}
*{box-sizing:border-box;margin:0;padding:0}
html,body{width:1200px;height:4264px;overflow:hidden}
body{position:relative;background:var(--white);font-family:"Open Sans",Arial,sans-serif;color:var(--ink)}
.abs{position:absolute}

/* city strip */
.city-strip{top:0;left:0;width:1200px;height:32px;display:flex;justify-content:center;gap:26px;align-items:center;font-size:11px;color:var(--blue-dark);border-bottom:1px solid #eee}
.city-strip .active{font-weight:700;color:var(--navy)}

/* header */
.brand{top:50px;left:640px;display:flex;align-items:center;gap:10px}
.brand-dot{width:46px;height:46px;border-radius:50%;background:var(--blue)}
.brand-name{font-size:34px;font-weight:700;color:var(--blue-dark);letter-spacing:-0.5px}
.brand-tag{top:102px;left:700px;font-size:10px;color:var(--grey-text)}
.nav{top:142px;left:180px;display:flex;height:40px;font-size:12px}
.nav a{display:flex;flex-direction:column;justify-content:center;padding:0 14px;color:var(--navy);font-weight:700;text-decoration:none;line-height:1.15}
.nav a small{font-weight:400;font-size:9px;color:var(--grey-text)}
.nav a.home{border-bottom:3px solid var(--blue);color:var(--blue)}
.nav a.login{background:var(--blue-dark);color:var(--white)}
.nav a.register{background:var(--panel-dark);color:var(--white)}
.promo-note{top:184px;left:955px;font-size:9px;color:var(--accent)}

.side-tab{top:210px;left:0;width:30px;height:160px;background:var(--blue-dark);color:var(--white);font-size:11px;font-weight:600;writing-mode:vertical-rl;transform:rotate(180deg);display:flex;align-items:center;justify-content:center}

/* hero */
.hero{top:198px;left:180px;width:900px;height:372px;
  background:linear-gradient(100deg,#2f7fd0 0%,#5aa6e6 18%,#d9c7a6 36%,#e04b4b 48%,#f2b632 58%,#3bb0e0 68%,#7dbf4a 78%,#c9b08a 90%,#8a7358 100%)}
.hero-title{top:224px;left:204px;font-size:22px;font-weight:600;color:var(--white);text-shadow:0 1px 3px rgba(0,0,0,.35)}
.hero-arrow{top:360px;width:28px;height:40px;background:rgba(60,60,60,.85);display:flex;align-items:center;justify-content:center}
.hero-arrow.prev{left:150px}.hero-arrow.next{left:1052px}

.search{top:570px;left:180px;width:900px;height:92px;background:var(--blue-dark);color:var(--white);padding:12px 18px}
.search h3{font-size:13px;font-weight:700}
.search p{font-size:9px;opacity:.8}
.search-types{top:16px;left:300px;display:flex;gap:18px;font-size:11px}
.search-types span::before{content:"";display:inline-block;width:10px;height:10px;background:var(--white);margin-right:5px;vertical-align:-1px}
.search-fields{top:50px;left:18px;display:flex;gap:10px}
.field{width:200px;height:28px;background:var(--white);color:#888;font-size:10px;display:flex;align-items:center;padding:0 8px}
.field.wide{width:250px}
.search-btn{top:0;right:0;width:34px;height:92px;background:var(--panel-dark);writing-mode:vertical-rl;font-size:11px;font-weight:700;display:flex;align-items:center;justify-content:center}

.cats{top:670px;left:180px;width:900px;display:flex;gap:10px}
.cat{flex:1;height:84px;background:var(--panel);color:var(--white);text-align:center;padding-top:20px;position:relative}
.cat b{display:block;font-size:13px;font-weight:600}
.cat i{font-style:normal;font-size:9px;opacity:.8;display:block;line-height:1.3;margin-top:4px}
.cat::after{content:"";position:absolute;left:50%;bottom:-10px;margin-left:-10px;border:10px solid transparent;border-bottom:0;border-top-color:var(--panel)}

/* section headings */
.sec-head{left:180px;display:flex;align-items:center;gap:14px}
.sec-head h2{font-size:24px;font-weight:600;color:var(--ink)}
.sec-head span{font-size:11px;color:var(--grey-text);border-left:1px solid #bbb;padding-left:12px}

/* cards */
.grid{left:180px;width:900px;display:grid;grid-template-columns:repeat(4,204px);column-gap:28px;row-gap:20px}
.card{height:330px;border:1px solid var(--line);background:var(--white);text-align:center;padding-top:14px}
.card h4{font-size:13px;font-weight:700}
.card .photo{width:180px;height:150px;margin:12px auto 12px}
.card .type{font-size:11px;color:var(--grey-text)}
.card svg{display:block;margin:12px auto 4px}
.card .loc{font-size:12px;font-weight:700;color:var(--blue)}
.card .view{font-size:10px;color:var(--grey-text);margin-top:8px}
.card.hot{background:var(--blue);border-color:var(--blue);color:var(--white)}
.card.hot .type,.card.hot .loc,.card.hot .view{color:var(--white)}
.p1{background:linear-gradient(160deg,#3f8fe0 0%,#9fd0f5 35%,#f0e4cf 60%,#c78a4a 100%)}
.p2{background:linear-gradient(170deg,#5fa8ea 0%,#cfe3f2 40%,#b5433a 70%,#6b4a36 100%)}
.p3{background:linear-gradient(180deg,#2f7fd6 0%,#7fb8ea 40%,#e8a64a 75%,#9a5e2a 100%)}
.p4{background:linear-gradient(180deg,#4a9be6 0%,#b9d8f0 45%,#8fa3b5 75%,#4d5b66 100%)}
.p5{background:linear-gradient(160deg,#79b7ec 0%,#e6d3b5 45%,#d2583a 75%,#6a4630 100%)}
.p6{background:linear-gradient(165deg,#4d9ae4 0%,#c2ddf2 40%,#e0b56c 70%,#7a5a3a 100%)}
.p7{background:linear-gradient(180deg,#3b8ae0 0%,#92c4ee 40%,#f0b45a 72%,#8c5a2c 100%)}
.p8{background:linear-gradient(180deg,#5aa3e8 0%,#c6def0 45%,#7fa9c9 72%,#3f5566 100%)}

/* mavens band */
.mavens-band{top:1714px;left:0;width:1200px;height:510px;background:linear-gradient(180deg,#1a8ee0,#0e5fa6)}
.mavens-photo{top:1812px;left:180px;width:240px;height:340px;background:linear-gradient(170deg,#e8d2b0 0%,#c9864a 35%,#b23a3a 60%,#5a3e30 100%)}
.mavens-title{top:1808px;left:440px;font-size:28px;font-weight:600;color:var(--white)}
.mavens-copy{top:1856px;left:440px;width:560px;font-size:13px;line-height:1.45;color:var(--white)}
.minput{height:32px;background:var(--white);font-size:11px;color:#888;padding:9px 10px}
.mavens-send{top:2104px;left:440px;width:80px;height:32px;background:var(--blue-dark);color:var(--white);font-size:12px;font-weight:600;display:flex;align-items:center;justify-content:center}

/* alert + editor */
.box{top:3060px;width:440px;height:560px;border:1px solid var(--line);background:var(--white);text-align:center;padding:34px 60px}
.box h3{font-size:28px;font-weight:600;color:var(--navy)}
.box p{font-size:11px;color:var(--grey-text);line-height:1.45;margin:10px 0 16px}
.sel{height:32px;border:1px solid var(--line);font-size:10px;color:#888;text-align:left;padding:9px 10px;margin-bottom:12px;position:relative}
.sel.drop::after{content:"";position:absolute;right:0;top:0;width:26px;height:30px;background:#888}
.btn{display:inline-block;background:var(--navy);color:var(--white);font-size:12px;font-weight:600;padding:9px 26px;margin-top:10px}
.fold{position:absolute;left:-1px;bottom:-1px;width:0;height:0;border-left:28px solid #9a9a9a;border-top:28px solid transparent}
.editor-photo{width:320px;height:200px;margin:18px auto 10px;background:linear-gradient(165deg,#6fb0e8 0%,#d8c6a8 40%,#d4473a 62%,#f0b13a 78%,#5e4a3a 100%)}

/* footer */
.footer{top:3760px;left:0;width:1200px;height:420px;background:var(--footer)}
.f-label{top:3790px;left:0;width:1200px;text-align:center;font-size:11px;color:#bbb}
.f-about{top:3816px;left:180px;width:900px;text-align:center;font-size:11px;line-height:1.55;color:#ccc}
.f-col{top:3900px;font-size:11px;line-height:1.9;color:#ccc}
.f-follow{top:3898px;left:530px;font-size:10px;color:#bbb}
.social{top:3922px;left:530px;display:flex;gap:10px}
.social span{width:26px;height:26px;border-radius:50%;border:1px solid #bbb}
.f-copy{top:3900px;left:860px;font-size:10px;color:#ccc;line-height:1.5}
.f-brand{top:3946px;left:860px;display:flex;align-items:center;gap:8px}
.f-brand span{width:28px;height:28px;border-radius:50%;background:var(--white)}
.f-brand b{font-size:22px;font-weight:700;color:var(--white)}
.bottom{top:4180px;left:0;width:1200px;height:84px;background:var(--blue-dark);color:var(--white);text-align:center;font-size:11px;line-height:1.5;padding-top:26px}
.pin-mark{top:4160px;left:586px}
</style>
</head>
<body>

<nav class="abs city-strip">
  <span class="active">Bangalore</span><span>Chennai</span><span>Greater Noida</span><span>Gurgaon</span><span>Hyderabad</span><span>Jaipur</span><span>Kolkata</span><span>Lucknow</span><span>Mumbai</span><span>Noida</span><span>Pune</span><span>Surat</span>
</nav>

<div class="abs brand"><span class="brand-dot"></span><span class="brand-name">lotvantage</span></div>
<div class="abs brand-tag">India's retail space marketplace</div>

<nav class="abs nav">
  <a class="home">Home</a>
  <a>Advertise with Us<small>Featured Listings · RMP</small></a>
  <a>Lot Mavens<small>Retail Space Advisors</small></a>
  <a>Listing Alert</a>
  <a class="login">Advertiser Login</a>
  <a class="register">New Advertiser - Register</a>
</nav>
<div class="abs promo-note">Get your property featured</div>

<div class="abs side-tab">Get in Touch</div>

<div class="abs hero" role="img" aria-label="Photo of a shopping complex with a multicoloured facade under a blue sky"></div>
<div class="abs hero-title">Shops at Rowan Park Bangalore</div>
<div class="abs hero-arrow prev"><svg width="10" height="14"><path d="M8 1 2 7l6 6" stroke="#fff" stroke-width="2" fill="none"/></svg></div>
<div class="abs hero-arrow next"><svg width="10" height="14"><path d="M2 1l6 6-6 6" stroke="#fff" stroke-width="2" fill="none"/></svg></div>

<section class="abs search">
  <h3>Select Retail Format</h3>
  <p>Choose one or more formats</p>
  <div class="abs search-types"><span>Retail Malls</span><span>High Street Shops</span><span>Shopping Complex</span><span>Retail Warehouses</span></div>
  <div class="abs search-fields">
    <div class="field">Enter Keywords</div>
    <div class="field">Select City</div>
    <div class="field">Select Area</div>
    <div class="field wide">Select Locality/Micro Market</div>
  </div>
  <div class="abs search-btn">SEARCH</div>
</section>

<div class="abs cats">
  <div class="cat"><b>Retail Malls</b><i>Browse leased and sale<br>units in malls</i></div>
  <div class="cat"><b>Shopping Complexes</b><i>Browse leased and sale<br>units in complexes</i></div>
  <div class="cat"><b>High Street Shops</b><i>Browse leased and sale<br>units on high streets</i></div>
  <div class="cat"><b>Retail Warehouses</b><i>Browse leased and sale<br>warehouse units</i></div>
</div>

<div class="abs sec-head" style="top:880px"><h2>Featured Retail Projects</h2><span>Across India</span></div>

<div class="abs grid" style="top:944px">
  <div class="card hot"><h4>Veltrona</h4><div class="photo p1" role="img" aria-label="Photo of mall exterior"></div><div class="type">Shopping Complex</div><svg width="14" height="18" viewBox="0 0 14 18"><path d="M7 0a7 7 0 0 0-7 7c0 5 7 11 7 11s7-6 7-11a7 7 0 0 0-7-7z" fill="#fff"/><circle cx="7" cy="7" r="2.5" fill="#1a8ee0"/></svg><div class="loc">Surat - Althan</div><div class="view">View this Listing »</div></div>
  <div class="card"><h4>Kavir 81 High Street</h4><div class="photo p2" role="img" aria-label="Photo of high street building"></div><div class="type">Shopping Complex</div><svg width="14" height="18" viewBox="0 0 14 18"><path d="M7 0a7 7 0 0 0-7 7c0 5 7 11 7 11s7-6 7-11a7 7 0 0 0-7-7z" fill="#1a8ee0"/><circle cx="7" cy="7" r="2.5" fill="#fff"/></svg><div class="loc">Surat - Althan</div><div class="view">View this Listing »</div></div>
  <div class="card"><h4>Arcus 24K</h4><div class="photo p3" role="img" aria-label="Photo of tall retail tower"></div><div class="type">Shopping Complex</div><svg width="14" height="18" viewBox="0 0 14 18"><path d="M7 0a7 7 0 0 0-7 7c0 5 7 11 7 11s7-6 7-11a7 7 0 0 0-7-7z" fill="#1a8ee0"/><circle cx="7" cy="7" r="2.5" fill="#fff"/></svg><div class="loc">Surat - Althan</div><div class="view">View this Listing »</div></div>
  <div class="card"><h4>Nerva Cosmopolitan</h4><div class="photo p4" role="img" aria-label="Photo of glass commercial building"></div><div class="type">Shopping Complex</div><svg width="14" height="18" viewBox="0 0 14 18"><path d="M7 0a7 7 0 0 0-7 7c0 5 7 11 7 11s7-6 7-11a7 7 0 0 0-7-7z" fill="#1a8ee0"/><circle cx="7" cy="7" r="2.5" fill="#fff"/></svg><div class="loc">Surat - Althan</div><div class="view">View this Listing »</div></div>
  <div class="card"><h4>Ostra Skywalk Mall</h4><div class="photo p5" role="img" aria-label="Photo of mall facade"></div><div class="type">Shopping Complex</div><svg width="14" height="18" viewBox="0 0 14 18"><path d="M7 0a7 7 0 0 0-7 7c0 5 7 11 7 11s7-6 7-11a7 7 0 0 0-7-7z" fill="#1a8ee0"/><circle cx="7" cy="7" r="2.5" fill="#fff"/></svg><div class="loc">Surat - Althan</div><div class="view">View this Listing »</div></div>
  <div class="card"><h4>Kavir 81 High Street</h4><div class="photo p6" role="img" aria-label="Photo of high street building"></div><div class="type">Shopping Complex</div><svg width="14" height="18" viewBox="0 0 14 18"><path d="M7 0a7 7 0 0 0-7 7c0 5 7 11 7 11s7-6 7-11a7 7 0 0 0-7-7z" fill="#1a8ee0"/><circle cx="7" cy="7" r="2.5" fill="#fff"/></svg><div class="loc">Surat - Althan</div><div class="view">View this Listing »</div></div>
  <div class="card"><h4>Arcus 24K</h4><div class="photo p7" role="img" aria-label="Photo of tall retail tower"></div><div class="type">Shopping Complex</div><svg width="14" height="18" viewBox="0 0 14 18"><path d="M7 0a7 7 0 0 0-7 7c0 5 7 11 7 11s7-6 7-11a7 7 0 0 0-7-7z" fill="#1a8ee0"/><circle cx="7" cy="7" r="2.5" fill="#fff"/></svg><div class="loc">Surat - Althan</div><div class="view">View this Listing »</div></div>
  <div class="card"><h4>Nerva Cosmopolitan</h4><div class="photo p8" role="img" aria-label="Photo of glass commercial building"></div><div class="type">Shopping Complex</div><svg width="14" height="18" viewBox="0 0 14 18"><path d="M7 0a7 7 0 0 0-7 7c0 5 7 11 7 11s7-6 7-11a7 7 0 0 0-7-7z" fill="#1a8ee0"/><circle cx="7" cy="7" r="2.5" fill="#fff"/></svg><div class="loc">Surat - Althan</div><div class="view">View this Listing »</div></div>
</div>

<section class="abs mavens-band"></section>
<div class="abs mavens-photo" role="img" aria-label="Photo of shoppers walking through a busy mall"></div>
<h2 class="abs mavens-title">Lot Mavens</h2>
<p class="abs mavens-copy">Post your Retail Space requirement with us and our experts shall get back with suitable options and even help you in your transaction. This is a free service!</p>
<div class="abs minput" style="top:1936px;left:440px;width:270px">Enter Email</div>
<div class="abs minput" style="top:1936px;left:720px;width:280px">Mobile</div>
<div class="abs minput" style="top:1980px;left:440px;width:560px;height:110px">Message</div>
<div class="abs mavens-send">Send</div>

<div class="abs sec-head" style="top:2316px"><h2>Featured New Launches</h2><span>Across India</span></div>

<div class="abs grid" style="top:2380px">
  <div class="card hot"><h4>Veltrona</h4><div class="photo p1" role="img" aria-label="Photo of mall exterior"></div><div class="type">Shopping Complex</div><svg width="14" height="18" viewBox="0 0 14 18"><path d="M7 0a7 7 0 0 0-7 7c0 5 7 11 7 11s7-6 7-11a7 7 0 0 0-7-7z" fill="#fff"/><circle cx="7" cy="7" r="2.5" fill="#1a8ee0"/></svg><div class="loc">Surat - Althan</div><div class="view">View this Listing »</div></div>
  <div class="card"><h4>Kavir 81 High Street</h4><div class="photo p2" role="img" aria-label="Photo of high street building"></div><div class="type">Shopping Complex</div><svg width="14" height="18" viewBox="0 0 14 18"><path d="M7 0a7 7 0 0 0-7 7c0 5 7 11 7 11s7-6 7-11a7 7 0 0 0-7-7z" fill="#1a8ee0"/><circle cx="7" cy="7" r="2.5" fill="#fff"/></svg><div class="loc">Surat - Althan</div><div class="view">View this Listing »</div></div>
  <div class="card"><h4>Arcus 24K</h4><div class="photo p3" role="img" aria-label="Photo of tall retail tower"></div><div class="type">Shopping Complex</div><svg width="14" height="18" viewBox="0 0 14 18"><path d="M7 0a7 7 0 0 0-7 7c0 5 7 11 7 11s7-6 7-11a7 7 0 0 0-7-7z" fill="#1a8ee0"/><circle cx="7" cy="7" r="2.5" fill="#fff"/></svg><div class="loc">Surat - Althan</div><div class="view">View this Listing »</div></div>
  <div class="card"><h4>Nerva Cosmopolitan</h4><div class="photo p4" role="img" aria-label="Photo of glass commercial building"></div><div class="type">Shopping Complex</div><svg width="14" height="18" viewBox="0 0 14 18"><path d="M7 0a7 7 0 0 0-7 7c0 5 7 11 7 11s7-6 7-11a7 7 0 0 0-7-7z" fill="#1a8ee0"/><circle cx="7" cy="7" r="2.5" fill="#fff"/></svg><div class="loc">Surat - Althan</div><div class="view">View this Listing »</div></div>
  <div class="card"><h4>Ostra Skywalk Mall</h4><div class="photo p5" role="img" aria-label="Photo of mall facade"></div><div class="type">Shopping Complex</div><svg width="14" height="18" viewBox="0 0 14 18"><path d="M7 0a7 7 0 0 0-7 7c0 5 7 11 7 11s7-6 7-11a7 7 0 0 0-7-7z" fill="#1a8ee0"/><circle cx="7" cy="7" r="2.5" fill="#fff"/></svg><div class="loc">Surat - Althan</div><div class="view">View this Listing »</div></div>
  <div class="card"><h4>Kavir 81 High Street</h4><div class="photo p6" role="img" aria-label="Photo of high street building"></div><div class="type">Shopping Complex</div><svg width="14" height="18" viewBox="0 0 14 18"><path d="M7 0a7 7 0 0 0-7 7c0 5 7 11 7 11s7-6 7-11a7 7 0 0 0-7-7z" fill="#1a8ee0"/><circle cx="7" cy="7" r="2.5" fill="#fff"/></svg><div class="loc">Surat - Althan</div><div class="view">View this Listing »</div></div>
  <div class="card"><h4>Arcus 24K</h4><div class="photo p7" role="img" aria-label="Photo of tall retail tower"></div><div class="type">Shopping Complex</div><svg width="14" height="18" viewBox="0 0 14 18"><path d="M7 0a7 7 0 0 0-7 7c0 5 7 11 7 11s7-6 7-11a7 7 0 0 0-7-7z" fill="#1a8ee0"/><circle cx="7" cy="7" r="2.5" fill="#fff"/></svg><div class="loc">Surat - Althan</div><div class="view">View this Listing »</div></div>
  <div class="card"><h4>Nerva Cosmopolitan</h4><div class="photo p8" role="img" aria-label="Photo of glass commercial building"></div><div class="type">Shopping Complex</div><svg width="14" height="18" viewBox="0 0 14 18"><path d="M7 0a7 7 0 0 0-7 7c0 5 7 11 7 11s7-6 7-11a7 7 0 0 0-7-7z" fill="#1a8ee0"/><circle cx="7" cy="7" r="2.5" fill="#fff"/></svg><div class="loc">Surat - Althan</div><div class="view">View this Listing »</div></div>
</div>

<section class="abs box" style="left:180px">
  <h3>Listing Alert</h3>
  <p>Register for fortnightly email updates on New Listings at Lotvantage</p>
  <div class="sel">Enter Email</div>
  <div class="sel drop">Select Type of Interest</div>
  <div class="sel drop">Select City</div>
  <div class="sel drop">Select Locality</div>
  <div class="btn">Subscribe</div>
  <span class="fold"></span>
</section>

<section class="abs box" style="left:640px">
  <h3>Editor's Choice</h3>
  <div class="editor-photo" role="img" aria-label="Photo of a busy shopping street with colourful storefronts"></div>
  <p>A "Select" listing of retail properties handpicked by our editors, based on location, access, footfall potential and developer track record.</p>
  <div class="btn">More</div>
  <span class="fold"></span>
</section>

<footer class="abs footer"></footer>
<div class="abs f-label">About Lotvantage</div>
<p class="abs f-about">Lotvantage.com is a specialised web based platform for retail space, featuring properties across India under various formats such as Retail Malls, Shopping Complexes, High Street Shops. Also featured are Retail Warehouses which provide the logistic back-end for the retail business. Lotvantage.com is useful to various categories of users as follows: a. Retailers b. Investors c. Brokers</p>
<div class="abs f-col" style="left:180px">About Us<br>Privacy Policy<br>Terms of Use<br>Contact Us<br>Site Map</div>
<div class="abs f-col" style="left:320px">Retail Malls<br>Shopping Complex<br>High Street Shops<br>Retail Warehouses</div>
<div class="abs f-follow">Follow us on</div>
<div class="abs social"><span></span><span></span><span></span><span></span><span></span></div>
<div class="abs f-copy">Copyright © 2015 Retail Grid India<br>All rights reserved</div>
<div class="abs f-brand"><span></span><b>lotvantage</b></div>

<div class="abs bottom">Retail Grid India · Unit 12, 2nd Floor, Maple Court, Ridge Road, Gurgaon - 122000<br>Phone: 0124-5550182 · Email: hello@lotvantage.com</div>
<svg class="abs pin-mark" width="28" height="36" viewBox="0 0 14 18"><path d="M7 0a7 7 0 0 0-7 7c0 5 7 11 7 11s7-6 7-11a7 7 0 0 0-7-7z" fill="#fff"/><circle cx="7" cy="7" r="2.5" fill="#0f63a8"/></svg>

</body>
</html>
```